Logo and business card for optometric practice
Calvin Mortenhall & Associates
Petra Valunkova, O.D.
Simon Orchardt, O.D.
Neil Tabarrou, O.D.
417 Meadowbrook Parkway
Ashfield Terrace, New York 11498
516-555-0142

Target Market(s)

Patients, general public

Industry/Entity Type

Business

Logo Text

Calvin Mortenhall & Associates Optometrists

Logo styles of interest
Pictorial/Combination Logo
Font styles to use
Serif
Sans Serif

Requirements
Must have
• current inspiration: realistic or photo closeup of eye, with interesting treatment of the iris OR
tech look, with closeup of eye and grid like the doctor is looking through a camera or microscope to view the eye up close
Should not have
• NO cartoons

```html
<!DOCTYPE html>
<html lang="en">
<head>
<meta charset="utf-8">
<title>Calvin Mortenhall &amp; Associates — Business Card</title>
<link href="https://fonts.googleapis.com/css2?family=Crimson+Text:wght@400&family=Open+Sans:wght@300;400&display=swap" rel="stylesheet">
<style>
  :root {
    --page-bg: #e9e8e6;
    --card-bg: #ffffff;
    --card-shade: #f1f1f1;
    --brand-blue: #2a9fd2;
    --brand-blue-light: #7cc6e6;
    --ink-dark: #3d3d3d;
    --ink-soft: #6a6a6a;
    --rule: #9a9a9a;
    --photo-light: #e7e4e2;
    --photo-mid: #c9c6c4;
  }
  * { margin: 0; padding: 0; box-sizing: border-box; }
  html, body { width: 704px; height: 1200px; overflow: hidden; }
  body {
    background: var(--page-bg);
    position: relative;
    font-family: "Open Sans", Arial, sans-serif;
  }
  .card {
    position: absolute;
    left: 52px;
    width: 600px;
    height: 343px;
    background: linear-gradient(135deg, var(--card-bg) 40%, var(--card-shade));
    box-shadow: 0 6px 18px rgba(0,0,0,0.18);
    overflow: hidden;
  }
  .card--front { top: 128px; }
  .card--back { top: 729px; }

  .front-art { position: absolute; inset: 0; }

  .brand {
    position: absolute;
    display: flex;
    align-items: center;
    gap: 10px;
    font-family: "Crimson Text", Georgia, serif;
    font-size: 21px;
    white-space: nowrap;
  }
  .brand__mark {
    width: 22px; height: 22px;
    border-radius: 50%;
    background: var(--brand-blue);
  }
  .brand__name { color: var(--brand-blue); }
  .brand__suffix { color: var(--ink-dark); }

  .card--front .brand { right: 24px; bottom: 24px; }
  .card--back .brand { left: 40px; top: 46px; }

  .contact {
    position: absolute;
    right: 40px;
    top: 40px;
    text-align: right;
    font-size: 12.5px;
    line-height: 21px;
    color: var(--ink-dark);
  }
  .contact__line { display: flex; justify-content: flex-end; align-items: center; gap: 8px; }
  .contact__icon { width: 12px; height: 12px; flex: none; }
  .contact__line--plain { padding-right: 20px; }

  .divider {
    position: absolute;
    left: 40px; right: 40px;
    top: 118px;
    height: 1px;
    background: var(--rule);
  }

  .doctors {
    position: absolute;
    left: 40px;
    bottom: 44px;
    list-style: none;
    font-size: 14px;
    font-weight: 300;
    line-height: 21px;
    color: var(--ink-soft);
    padding-bottom: 8px;
    border-bottom: 1px solid var(--rule);
    width: 200px;
  }
</style>
</head>
<body>

  <section class="card card--front">
    <svg class="front-art" width="600" height="343" viewBox="0 0 600 343">
      <defs>
        <linearGradient id="photoTone" x1="0" y1="0" x2="1" y2="1">
          <stop offset="0" stop-color="var(--photo-light)"/>
          <stop offset="1" stop-color="var(--photo-mid)"/>
        </linearGradient>
      </defs>
      <path d="M0,0 H564 C484,160 284,280 124,343 H0 Z" fill="var(--brand-blue-light)" opacity="0.55"/>
      <path d="M0,0 H552 C472,160 272,280 112,343 H0 Z" fill="var(--brand-blue)"/>
      <path d="M0,0 H540 C460,160 260,280 100,343 H0 Z" fill="url(#photoTone)"
            role="img" aria-label="Photograph of an optometrist examining a patient's eye through a slit-lamp microscope"/>
    </svg>
    <div class="brand">
      <span class="brand__mark"></span>
      <span><span class="brand__name">Calvin Mortenhall</span> <span class="brand__suffix">&amp; Associates</span></span>
    </div>
  </section>

  <section class="card card--back">
    <div class="brand">
      <span class="brand__mark"></span>
      <span><span class="brand__name">Calvin Mortenhall</span> <span class="brand__suffix">&amp; Associates</span></span>
    </div>

    <div class="contact">
      <div class="contact__line">
        <span>516-555-0142</span>
        <svg class="contact__icon" viewBox="0 0 12 12"><rect x="0" y="0" width="12" height="12" rx="2" fill="var(--brand-blue)"/><path d="M3.5,2.5 l1.5,0 l0.7,2 l-1,0.8 a5,5 0 0 0 2,2 l0.8,-1 l2,0.7 l0,1.5 a1,1 0 0 1 -1,1 a6.5,6.5 0 0 1 -6,-6 a1,1 0 0 1 1,-1z" fill="#fff"/></svg>
      </div>
      <div class="contact__line">
        <span>417 Meadowbrook Parkway</span>
        <svg class="contact__icon" viewBox="0 0 12 12"><path d="M6,0.5 a4,4 0 0 1 4,4 c0,3 -4,7 -4,7 s-4,-4 -4,-7 a4,4 0 0 1 4,-4z" fill="var(--brand-blue)"/><circle cx="6" cy="4.5" r="1.5" fill="#fff"/></svg>
      </div>
      <div class="contact__line contact__line--plain">
        <span>Ashfield Terrace, New York 11498</span>
      </div>
    </div>

    <div class="divider"></div>

    <ul class="doctors">
      <li>Petra Valunkova, O.D.</li>
      <li>Simon Orchardt, O.D.</li>
      <li>Neil Tabarrou, O.D.</li>
    </ul>
  </section>

</body>
</html>
```